Bluvora business website

I am wanting a website for my media agency Bluvora.

It needs to be be an attractive, unique and professional looking website. The website is a destination for people to be able to understand the service that Bluvora offers.

Please read uploaded website copy to gain an understanding of the business.

Target Market(s)

small business owners, business decision makers, marketing managers,

Industry/Entity Type

Business

Requirements
Must have
• Good branding.

```html
<!DOCTYPE html>
<html lang="en">
<head>
<meta charset="utf-8">
<title>Bluvora — About Us</title>
<link rel="stylesheet" href="https://fonts.googleapis.com/css2?family=Arimo:wght@400&family=Cinzel:wght@400;500&display=swap">
<style>
:root{
  --header-top:#f2f2f2;
  --header-bottom:#cfcfcf;
  --nav-top:#6a6a6a;
  --nav-bottom:#3a3a3a;
  --teal:#2b7d9b;
  --teal-deep:#1d6585;
  --sky-light:#d9ecf6;
  --sky-mid:#a9d0e6;
  --dark-top:#22383f;
  --dark-bottom:#0c1e25;
  --text-dark:#444;
  --text-light:#e8eef0;
  --heading:#555;
  --brand:#4a56a8;
  --footer-bg:#e4e4e4;
  --footer-text:#555;
  --btn:#9a9a9a;
}
*{box-sizing:border-box;margin:0;padding:0}
html,body{width:992px;height:1200px;overflow:hidden}
body{position:relative;font-family:"Arimo",Arial,sans-serif;color:var(--text-dark);background:var(--teal)}
.site-header{position:absolute;left:0;top:0;width:992px;height:139px;background:linear-gradient(var(--header-top),var(--header-bottom));border-top:5px solid #555}
.brand{position:absolute;left:447px;top:16px;display:flex;align-items:center;gap:6px}
.brand-mark{width:14px;height:14px;background:var(--brand)}
.brand-name{font-size:22px;color:var(--brand)}
.contact{position:absolute;left:708px;top:46px;font-size:14px;color:#555;line-height:22px}
.contact-row{display:flex;align-items:center;gap:8px}
.contact svg{width:18px;height:16px;fill:#555}
.main-nav{position:absolute;left:0;top:139px;width:992px;height:37px;background:linear-gradient(var(--nav-top),var(--nav-bottom));border-bottom:1px solid #222}
.main-nav a{position:absolute;top:10px;color:#eee;font-size:14px;text-decoration:none}
.search{position:absolute;left:705px;top:5px;width:159px;height:26px;background:#fff;border:1px solid #ccc;font-size:12px;color:#aaa;padding:5px 6px}
.search svg{position:absolute;right:8px;top:7px;width:10px;height:10px;stroke:#aaa;fill:none}
.stage{position:absolute;left:0;top:177px;width:992px;height:961px;background:linear-gradient(var(--teal),var(--teal-deep))}
.panel{position:absolute;left:39px;top:0;width:914px;height:620px;background:linear-gradient(180deg,#cfe6f3 0,#cfe6f3 40px,#f6fafc 40px,#f6fafc 251px,#dceef7 251px,#a8cfe6 620px)}
.waves{position:absolute;left:39px;top:480px}
.about{position:absolute;left:225px;top:227px;width:563px}
.about h1{font-family:"Cinzel",serif;font-weight:500;font-size:22px;color:var(--heading);text-align:center;padding-bottom:6px;border-bottom:1px solid #aaa}
.about p{font-size:12px;line-height:16.6px;margin-top:16px;padding-left:2px}
.video{position:absolute;left:262px;top:360px;width:456px;height:277px;border:3px solid #9cc2d2;background:#222}
.video-art{position:absolute;left:0;top:0;width:450px;height:247px;background:linear-gradient(120deg,#fafafa 30%,#e3e6ea 70%,#c9cdd6)}
.play{position:absolute;left:199px;top:108px;width:62px;height:42px;border-radius:10px;background:#2a2a2a}
.play::after{content:"";position:absolute;left:25px;top:13px;border-left:15px solid #fff;border-top:8px solid transparent;border-bottom:8px solid transparent}
.controls{position:absolute;left:0;top:247px;width:450px;height:24px;background:#1b1b1b;color:#ddd;font-size:8px}
.progress{position:absolute;left:0;top:0;width:450px;height:4px;background:#555}
.progress span{display:block;width:70px;height:4px;background:#c00}
.time{position:absolute;left:66px;top:9px}
.services{position:absolute;left:0;top:0}
.photo{position:absolute;width:160px;height:160px;border-radius:50%;border:3px solid #d8e6ec}
.photo-ring{position:absolute;width:176px;height:176px;border-radius:50%;border:1px dashed #8aa8b6}
.service{position:absolute;width:240px;color:var(--text-light)}
.service h2{font-family:"Cinzel",serif;font-weight:500;font-size:20px;line-height:22px;color:#fff}
.service p{font-size:12px;line-height:19px;margin-top:10px;text-align:justify;height:95px;overflow:hidden;padding-left:2px}
.read-more{display:block;width:84px;height:18px;background:var(--btn);color:#eee;font-size:9px;text-align:center;line-height:18px;text-decoration:none;border:1px solid #777}
.site-footer{position:absolute;left:0;top:1138px;width:992px;height:62px;background:var(--footer-bg);font-size:12px;color:var(--footer-text)}
.footer-nav{position:absolute;left:75px;top:13px;word-spacing:2px}
.footer-nav a{color:var(--footer-text);text-decoration:none}
.footer-nav i{font-style:normal;margin:0 10px}
.copyright{position:absolute;left:76px;top:40px;font-size:11px}
.social{position:absolute;left:754px;top:14px;display:flex;gap:9px}
.social span{width:27px;height:27px;border-radius:50%;background:#999}
.social span:last-child{background:#666}
</style>
</head>
<body>
<header class="site-header">
  <div class="brand"><span class="brand-mark"></span><span class="brand-name">Bluvora</span></div>
  <div class="contact">
    <div class="contact-row"><svg viewBox="0 0 16 16"><path d="M3 1l3 3-2 2c1 2 3 4 5 5l2-2 3 3-2 3C7 15 1 9 1 3z"/></svg>1234-456-789</div>
    <div class="contact-row"><svg viewBox="0 0 16 16"><path d="M1 4h14v9H1z M1 4l7 5 7-5" stroke="#eee" stroke-width="1"/></svg>Name@email.com</div>
  </div>
</header>
<nav class="main-nav">
  <a style="left:108px">Home</a><a style="left:195px">About</a><a style="left:283px">What We Do</a><a style="left:412px">People</a><a style="left:507px">Ideas</a><a style="left:587px">Contact Us</a>
  <div class="search">Search<svg viewBox="0 0 10 10"><circle cx="6" cy="4" r="3"/><path d="M4 6L1 9"/></svg></div>
</nav>
<main class="stage">
  <div class="panel"></div>
  <svg class="waves" width="914" height="481" viewBox="0 0 914 481">
    <path d="M0 20 C150 -10 280 40 420 30 C560 20 700 -10 914 40 V481 H0Z" fill="#c8e1f0"/>
    <path d="M0 60 C180 30 300 80 460 60 C620 40 760 30 914 70 V481 H0Z" fill="#b5d6ea"/>
    <rect x="0" y="140" width="914" height="341" fill="url(#dark)"/>
    <path d="M0 420 Q457 490 914 420 V481 H0Z" fill="var(--teal-deep)"/>
    <defs><linearGradient id="dark" x1="0" y1="0" x2="0" y2="1"><stop offset="0" stop-color="#22383f"/><stop offset="1" stop-color="#0c1e25"/></linearGradient></defs>
  </svg>
</main>
<section class="about">
  <h1>About Us</h1>
  <p>Bluvora is a media strategy, planning and buying agency. We work with both small and big businesses. Bluvora works across all offline platforms (radio, press, outdoor &amp; TV), search engine marketing, online display, email, social &amp; mobile. We attain a high level of value for our clients with a focus on integration.</p>
  <p>We are marketing partners in our clients businesses and enjoy seeing them grow and achieve their goals.</p>
</section>
<div class="video">
  <div class="video-art" role="img" aria-label="Video still: rising green arrow over a growing bar chart"></div>
  <div class="play"></div>
  <div class="controls"><div class="progress"><span></span></div><span class="time">0:15 / 0:39</span></div>
</div>
<section class="services">
  <div class="photo-ring" style="left:137px;top:697px"></div>
  <div class="photo" role="img" aria-label="Photo of a planning meeting over papers and coffee" style="left:145px;top:705px;background:radial-gradient(#f2f2f2,#9aa0a6)"></div>
  <div class="photo-ring" style="left:397px;top:697px"></div>
  <div class="photo" role="img" aria-label="Black and white photo of a training session in an office" style="left:405px;top:705px;background:radial-gradient(#cfcfcf,#4a4a4a)"></div>
  <div class="photo-ring" style="left:676px;top:697px"></div>
  <div class="photo" role="img" aria-label="Photo of a hand touching a social network diagram" style="left:684px;top:705px;background:radial-gradient(#9a8fb8,#2e2a52)"></div>

  <div class="service" style="left:122px;top:876px">
    <h2>Media Strategy &amp;<br>Planning</h2>
    <p>Using accurate analysis we provide relevant research about the consumer or business target &amp; trends in the market place. A tailored strategy is devised that comprises of the right</p>
    <a class="read-more" href="#" style="margin-left:51px">read more</a>
  </div>
  <div class="service" style="left:394px;top:880px;width:250px">
    <h2>Media Training &amp;<br>Campaign Monitoring</h2>
    <p style="width:200px">Using our media partner relation-ships, trade negotiation techniques &amp; experience we achieve a high level of value for all media buys that leads to significant cost savings for clients.</p>
    <a class="read-more" href="#" style="margin-left:54px">read more</a>
  </div>
  <div class="service" style="left:670px;top:882px;width:220px">
    <h2>Content &amp; Creative</h2>
    <p style="width:210px;height:113px">Creating imaginative &amp; interesting con-tent for a brand can be a great way of achieving a high level of engagement to a target audience. Content can be pub-lished and broadcast on a variety of</p>
    <a class="read-more" href="#" style="margin-left:63px">read more</a>
  </div>
</section>
<footer class="site-footer">
  <div class="footer-nav"><a>Home</a><i>|</i><a>About</a><i>|</i><a>What We Do</a><i>|</i><a>People</a><i>|</i><a>Ideas</a><i>|</i><a>Contat us</a></div>
  <div class="copyright">Bluvora 2013 Copyright All rights reserved.</div>
  <div class="social"><span></span><span></span><span></span><span></span></div>
</footer>
</body>
</html>
```